Wealth management firm needs a business card design

Using my logo, create a business card that covers all of the regulatory wordings that I need. It must have - Registered Office 7-9 Pelgrove Wynd, Edinburgh, EH4 2QN. Registered in Scotland under number SC804317. VORELT Wealth Management Ltd is an appointed representative of Kestoby wealth management Ltd, which is authorised and regulated by the Monetary Oversight Council.

Target Market(s)

professional clients

Industry/Entity Type

finance

Contact Information for Business Card

VORELT Wealth Management, Conor Tresk-Whitlaw, Director, 5 Dunmore Row, Edinburgh, EH9 4RT. 07812 459 163, conor.tresk-whitlaw@vorelt-example.com , www.vorelt-example.com

Font styles to use
Serif

Colors
0054AA
0677BA
7BADD7
CADEEF
E8F1F8

Requirements
Must have
• regulatory wording in small text at bottom

```html
<!DOCTYPE html>
<html lang="en">
<head>
<meta charset="utf-8">
<title>VORELT Wealth Management – Business Card</title>
<link rel="stylesheet" href="https://fonts.googleapis.com/css2?family=Noto+Serif:wght@400;700&display=swap">
<style>
  :root {
    --brand-blue: #0054AA;
    --bright-blue: #0677BA;
    --ink: #1d1f24;
    --card: #f2f2f0;
    --backdrop: #d9dadc;
    --serif: "Noto Serif", Georgia, serif;
  }
  * { box-sizing: border-box; margin: 0; padding: 0; }
  html, body { width: 1200px; height: 800px; overflow: hidden; }
  body {
    background: var(--backdrop);
    font-family: var(--serif);
    color: var(--ink);
    position: relative;
  }
  .card {
    position: absolute;
    top: 219px;
    width: 560px;
    height: 362px;
    background: var(--card);
    box-shadow: 0 6px 18px rgba(0,0,0,0.18);
  }
  .card--front { left: 27px; }
  .card--back { left: 613px; }

  /* Brand mark */
  .brand-mark {
    position: absolute;
    display: flex;
    align-items: center;
    gap: 8px;
    color: var(--bright-blue);
    font-weight: 700;
    letter-spacing: 0.06em;
  }
  .brand-mark__dot {
    display: inline-block;
    border-radius: 50%;
    background: var(--bright-blue);
  }
  .card--front .brand-mark { top: 48px; right: 48px; font-size: 20px; }
  .card--front .brand-mark__dot { width: 14px; height: 14px; }

  /* Front */
  .holder {
    position: absolute;
    left: 72px;
    top: 112px;
  }
  .holder__name {
    color: var(--bright-blue);
    font-weight: 700;
    font-size: 22px;
    letter-spacing: 0.01em;
    text-transform: uppercase;
  }
  .holder__role { font-size: 15px; margin-top: 2px; }

  .contact {
    position: absolute;
    left: 72px;
    right: 40px;
    bottom: 46px;
    font-size: 15px;
    line-height: 1.45;
  }
  .contact__web {
    display: flex;
    align-items: flex-end;
    gap: 14px;
    margin-bottom: 12px;
  }
  .contact__rule {
    flex: 0 0 130px;
    height: 1.5px;
    background: var(--bright-blue);
    margin-bottom: -8px;
  }
  .contact__url {
    margin-left: auto;
    white-space: nowrap;
    letter-spacing: 0.1em;
  }
  .contact__url strong { color: var(--bright-blue); font-weight: 700; }
  .contact__line { letter-spacing: 0.02em; white-space: nowrap; }
  .contact__line--mail { letter-spacing: 0.04em; }

  /* Back */
  .card--back .brand-mark {
    top: 58px;
    left: 0; right: 0;
    justify-content: center;
    font-size: 26px;
  }
  .card--back .brand-mark__dot { width: 18px; height: 18px; }

  .company {
    position: absolute;
    top: 128px;
    left: 0; right: 0;
    text-align: center;
  }
  .company__name { font-size: 28px; font-weight: 400; letter-spacing: 0.01em; }
  .company__tagline {
    font-size: 10px;
    letter-spacing: 0.04em;
    margin-top: 2px;
    padding-left: 120px;
  }

  .regulatory {
    position: absolute;
    left: 0;
    right: 0;
    bottom: 40px;
    display: flex;
    justify-content: center;
  }
  .regulatory__text {
    font-size: 11px;
    line-height: 1.45;
    text-align: left;
  }
  .regulatory__text span { display: block; white-space: nowrap; }
</style>
</head>
<body>

<section class="card card--front" aria-label="Business card front">
  <div class="brand-mark"><span class="brand-mark__dot"></span>VORELT</div>
  <div class="holder">
    <h1 class="holder__name">Conor Tresk-Whitlaw</h1>
    <p class="holder__role">Director</p>
  </div>
  <div class="contact">
    <p class="contact__web"><span class="contact__rule"></span><span class="contact__url">www.<strong>vorelt-example</strong>.com</span></p>
    <p class="contact__line">07812 459 163 &nbsp;/&nbsp; 5 Dunmore Row, Edinburgh, EH9 4RT</p>
    <p class="contact__line contact__line--mail">E-mail: conor.tresk-whitlaw@vorelt-example.com</p>
  </div>
</section>

<section class="card card--back" aria-label="Business card back">
  <div class="brand-mark"><span class="brand-mark__dot"></span>VORELT</div>
  <div class="company">
    <h2 class="company__name">VORELT Wealth Management Ltd</h2>
    <p class="company__tagline">Personal Financial Advice</p>
  </div>
  <div class="regulatory">
    <p class="regulatory__text">
      <span>Registered Office: 7-9 Pelgrove Wynd, Edinburgh, EH4 2QN.</span>
      <span>Registered in Scotland under number SC804317. VORELT Wealth Management</span>
      <span>Ltd is an appointed representative of Kestoby wealth management Ltd, which</span>
      <span>is authorised and regulated by the Monetary Oversight Council.</span>
    </p>
  </div>
</section>

</body>
</html>
```